Storage Company Newsletter

We need a design for a newsletter for our company Vaultnest, a digital and physical asset storage company .The newsletter will be informative and educational covering tips on secure storage of personal documents and items both at home and at the work place. Rest easy with Vaultnest is our mantra. We have a pre-existing trademark & logo. Colors are blue and green. We can share the cmyk/rgb color information and background is grey.

Target Market(s)

Mass market – Middle to High income individuals

Industry/Entity Type

Digital

Font styles to use
Sans Serif

Colors
0393ce
00a88f
edf2f7

Requirements
Must have
• The newsletter linked to a CMS. In HTML5; Mail-chimp integration readable on Gmail, Yahoo, Hotmail and Outlook
Nice to have
• Sections of the newsletter are:
• Cover story
• News Flash
• Mwanachi Perspective
• Spotlight on the Counties
• CEO's Corner
• Tips and Helpful Information
• Important Dates and Events

```html
<!DOCTYPE html>
<html lang="en">
<head>
<meta charset="utf-8">
<title>Vaultnest Newsletter</title>
<link href="https://fonts.googleapis.com/css2?family=Roboto:wght@400;500;700;900&display=swap" rel="stylesheet">
<style>
:root{
  --blue:#3d8fd8;
  --green:#00a88f;
  --cyan:#4dc3d3;
  --panel:#676c73;
  --canvas:#ffffff;
  --page:#ffffff;
  --ink:#2b2b2b;
  --muted:#555b61;
  --footer:#eeeff1;
  --rule:#e2e4e7;
}
*{box-sizing:border-box;margin:0;padding:0}
html,body{width:849px;height:1200px;overflow:hidden;background:var(--canvas);font-family:'Roboto',Arial,sans-serif;color:var(--ink)}
.board{position:relative;width:849px;height:1200px}
.panel{position:absolute;background:var(--panel)}
.panel--left{left:15px;top:0;width:400px;height:1200px}
.panel--right{left:415px;top:0;width:400px;height:1012px}
.topbar{position:absolute;left:95px;top:5px;width:237px;height:18px;background:var(--cyan);display:flex;justify-content:center;align-items:center;gap:6px}
.topbar svg{display:block}
.page{position:absolute;width:237px;background:var(--page)}
.page--left{left:95px;top:38px}
.page--right{left:502px;top:0}
.pad{padding:0 29px}
p{font-size:4.2px;line-height:6.8px;color:var(--muted)}
.btn{display:inline-block;background:var(--blue);color:#fff;font-size:3.8px;font-weight:500;padding:2.5px 7px;line-height:5px}
.btn--ghost{background:#fff;color:var(--ink);border:1px solid var(--ink);font-weight:700;padding:2px 6px}
.band{background:var(--blue);color:#fff;text-align:center;font-size:6px;font-weight:500;letter-spacing:.2px;display:flex;align-items:center;justify-content:center}
.item-title{color:var(--green);font-weight:700;font-size:5.8px;line-height:7.5px;margin-bottom:4px}
.meta{font-size:3.6px;color:var(--muted);margin-bottom:4px}
.link{color:var(--green);font-size:4.2px;display:block;margin-top:3px}
.photo{display:block}
.section-head{display:flex;justify-content:space-between;align-items:flex-start}
.heading{border-left:1.5px solid var(--ink);padding-left:5px;font-size:10px;font-weight:700;line-height:10px;text-transform:uppercase;color:#111}

.hero{position:relative;height:157px;background:linear-gradient(160deg,#2c5f9e 0%,#5e95d2 45%,#a9c8e8 100%)}
.hero__brand{position:absolute;left:8px;top:6px;display:flex;align-items:center;gap:3px;color:#fff;font-size:6px;font-weight:700}
.hero__brand i{width:18px;height:18px;background:var(--green);display:block}
.hero__nav{position:absolute;right:16px;top:13px;display:flex;gap:22px;font-size:4px;color:#fff;font-weight:500}
.hero__title{position:absolute;left:0;right:0;top:66px;text-align:center;color:#fff;font-size:11.5px;font-weight:900}
.hero__title span{color:var(--green)}
.hero__sub{position:absolute;left:48px;right:48px;top:89px;text-align:center;color:#fff;font-size:4.4px;line-height:7px}
.hero__cta{position:absolute;left:96px;top:117px;border:1px solid #fff;color:#fff;font-size:3.8px;padding:2px 6px}

.caring{height:160px;padding-top:15px}
.caring p{margin-top:20px}
.caring .photo{margin-top:13px;height:45px;background:linear-gradient(90deg,#6c6f72,#d9d4cc 40%,#2a2b2d 70%,#9a9a9a)}

.tips-band{height:63px;flex-direction:column;gap:10px;padding:0 29px;line-height:9px;font-size:6px}
.tips-band small{font-size:4.6px;font-weight:500}
.tips{height:250px;display:grid;grid-template-columns:1fr 1fr;column-gap:12px;grid-template-rows:repeat(3,82px);padding-top:8px}
.tip h4{color:var(--green);font-size:5.6px;margin-bottom:5px}

.clients{height:70px;flex-direction:column;gap:12px}
.clients__row{display:flex;gap:20px;font-size:4.4px;font-weight:500;align-items:center}
.clients__row span{display:flex;align-items:center;gap:2px}
.clients__row i{width:4px;height:4px;border-radius:50%;background:#fff;display:block}

.cover{height:235px;padding-top:15px}
.cover p.lead{margin-top:15px}
.duo{display:grid;grid-template-columns:1fr 1fr;gap:11px;margin-top:12px}
.duo .photo{height:58px;margin-bottom:8px}

.news{height:162px;padding-top:14px}
.news .photo{height:55px;background:linear-gradient(90deg,#8d8f93,#d6d6d4 30%,#6f7276 60%,#c9c7c3);margin-bottom:10px}
.trio{display:grid;grid-template-columns:repeat(3,1fr);gap:6px}
.trio .item-title{font-size:5.2px}
.trio .btn{margin-top:6px}

.spot-head{height:70px;background:linear-gradient(180deg,#1f2022,#4a4b4e);display:flex;flex-direction:column;align-items:center;justify-content:center;gap:8px;color:#fff;font-size:7px;font-weight:500;letter-spacing:.4px}
.spot{height:158px;padding-top:9px}
.spot__row{display:flex;gap:8px;align-items:flex-start;margin-bottom:12px}
.spot__row .photo{width:54px;height:40px;flex:none}
.spot__text{flex:1}
.spot__text .btn{margin-top:6px}

.mwan{height:177px;padding-top:8px}
.mwan .entry{margin-bottom:9px}
.mwan .btn{margin-top:5px}

.dates{height:98px;display:grid;grid-template-columns:1fr 1fr;gap:14px;padding-top:5px}
.dates .item-title{text-align:center;font-size:5.6px;line-height:7px;margin-bottom:2px}
.dates .btn{margin-top:6px}

.ceo{height:220px;padding-top:12px}
.ceo .photo{height:118px;margin-bottom:8px;background:linear-gradient(120deg,#c9d5e3,#eef2f6 40%,#a6b2c2 70%,#dfe5ec)}
.ceo .rule{border-top:1px solid var(--rule);margin-top:16px}

.signup{height:126px;padding-top:34px}
.signup .heading{font-size:9.5px;line-height:9.5px}
.signup__form{display:flex}
.signup__form span{border:1px solid #999;font-size:3.6px;padding:2px 3px;width:48px;color:var(--muted)}
.signup__form b{background:#111;color:#fff;font-size:3.6px;padding:2.5px 4px}
.signup p{margin-top:12px}

.footer{height:109px;background:var(--footer);padding:17px 29px 0 132px}
.footer h5{font-size:5px;font-weight:700;margin-bottom:6px}
.footer p{line-height:6.5px}
.footer p a{color:var(--green);text-decoration:none}
.socials{display:flex;gap:7px;margin-top:14px;margin-left:-54px}
.socials i{width:9px;height:9px;border:1px solid var(--blue);border-radius:50%;display:block}
</style>
</head>
<body>
<div class="board">
  <div class="panel panel--left"></div>
  <div class="panel panel--right"></div>

  <div class="topbar" aria-label="View options">
    <svg width="5" height="4" viewBox="0 0 5 4"><rect x=".3" y=".3" width="4.4" height="2.8" fill="none" stroke="#fff" stroke-width=".5"/></svg>
    <svg width="3" height="4" viewBox="0 0 3 4"><rect x=".3" y=".3" width="2.4" height="3.4" fill="none" stroke="#fff" stroke-width=".5"/></svg>
    <svg width="2" height="4" viewBox="0 0 2 4"><rect x=".3" y=".3" width="1.4" height="3.4" fill="none" stroke="#fff" stroke-width=".5"/></svg>
  </div>

  <main class="page page--left">
    <header class="hero" role="img" aria-label="Blue filing cabinets with open drawers">
      <div class="hero__brand"><i></i>Vaultnest</div>
      <nav class="hero__nav"><span>HOME</span><span>PORTFOLIO</span><span>CONTACT</span></nav>
      <h1 class="hero__title">REST EASY WITH <span>VAULTNEST</span></h1>
      <p class="hero__sub" style="color:#fff">Secure storage of personal documents and items both at home and at the work place</p>
      <span class="hero__cta">FIND OUT MORE</span>
    </header>

    <section class="caring pad">
      <div class="section-head">
        <h2 class="heading">Caring<br>for valuable<br>documents</h2>
        <span class="btn btn--ghost">MORE ABOUT US</span>
      </div>
      <p>Valuable documents include a wide range of items such as land title deeds, certificates, letters, photographs, newspaper cuttings and memorabilia. The longevity of these items can be threatened by numerous factors such as light, moisture, insects such as silverfish, and physical damage. By taking these simple precautions outlined below, you can preserve your valuable documents and keep them for posterity.</p>
      <div class="photo" role="img" aria-label="Embossed seals and stationery on a table"></div>
    </section>

    <div class="band tips-band">
      <div>SIMPLE PRECAUTION TO PRESERVE YOUR VALUABLE DOCUMENTS AND KEEP THEM FOR POSTERITY</div>
      <small>TIPS AND HELPFUL INFORMATION</small>
    </div>

    <section class="tips pad">
      <div class="tip"><h4># 1</h4><p>Valuable documents should be stored off the floor and away from external walls or windows, to protect them from dramatic fluctuations in temperature and humidity. Storage areas must remain dry to prevent mould growth and water damage.</p></div>
      <div class="tip"><h4># 2</h4><p>To avoid unnecessary wear and tear on original documents, make several copies for reference and circulation. Avoid continual copying of original documents. When photocopying, save an extra copy to make copies from in the future.</p></div>
      <div class="tip"><h4># 3</h4><p>Ensure that equipment such as scanners and photocopiers are clean before placing your documents on them. Alternatively, copying them inside a plastic sleeve will keep the documents clean and help to support fragile documents during copying.</p></div>
      <div class="tip"><h4># 4</h4><p>Valuable documents should be stored in protective plastic sleeves. Use well-fitting enclosures as folding weakens the paper and rolling can make it difficult to view the item without damaging it.</p></div>
      <div class="tip"><h4># 5</h4><p>Do not laminate your valuable documents. This is an irreversible process that permanently embeds the document in plastic and adhesive. Documents treated in this manner will become permanently disfigured.</p></div>
      <div class="tip"><h4># 6</h4><p>Never use metal paperclips, staples and pins. These can rust and cause irreversible staining to paper items. Sleeves are available that contain pockets of varying sizes so that diverse materials can be placed together in a binder or a storage box.</p></div>
    </section>

    <section class="band clients">
      <div>OUR CLIENTS</div>
      <div class="clients__row">
        <span><i></i>Dotline</span>
        <span>Kinetic Media</span>
        <span>Northvale Co</span>
        <span>Tandem</span>
      </div>
    </section>

    <section class="cover pad">
      <div class="section-head">
        <h2 class="heading">Cover<br>story</h2>
        <span class="btn btn--ghost">READ MORE</span>
      </div>
      <p class="lead">Nullam quis risus eget urna mollis ornare vel eu leo. Maecenas sed diam eget risus varius blandit sit amet non magna. Lorem ipsum dolor sit amet, consectetur adipiscing elit, sed do eiusmod tempor incididunt ut labore et dolore magna aliqua.</p>
      <div class="duo">
        <article>
          <div class="photo" role="img" aria-label="Brown expanding document file" style="background:linear-gradient(135deg,#f2f2f2,#9b7a55 45%,#5e4630 75%,#eeeeee)"></div>
          <h3 class="item-title">Secure Documents &amp; Assets Storage</h3>
          <div class="meta">Written by <b>Vaultnest</b> / February 2 2014</div>
          <p>Maecenas faucibus mollis interdum. Morbi leo risus, porta ac consectetur ac, vestibulum at eros. Aenean eu leo quam. Pellentesque ornare sem lacinia quam venenatis vestibulum.</p>
          <span class="link">Read more</span>
        </article>
        <article>
          <div class="photo" role="img" aria-label="Green box file with papers" style="background:linear-gradient(135deg,#f2f2f2,#cbb98f 40%,#2f6a60 70%,#eeeeee)"></div>
          <h3 class="item-title">Secure Documents &amp; Assets Storage</h3>
          <div class="meta">Written by <b>Vaultnest</b> / February 2 2014</div>
          <p>Maecenas faucibus mollis interdum. Morbi leo risus, porta ac consectetur ac, vestibulum at eros. Aenean eu leo quam. Pellentesque ornare sem lacinia quam venenatis vestibulum.</p>
          <span class="link">Read more</span>
        </article>
      </div>
    </section>

    <div class="band" style="height:30px">NEWS FLASH</div>

    <section class="news pad">
      <div class="photo" role="img" aria-label="Hands writing with a pen on paper"></div>
      <div class="trio">
        <article><h3 class="item-title">News Flash # 1</h3><p>Maecenas faucibus mollis interdum. Morbi leo risus, porta ac consectetur ac, vestibulum at eros.</p><span class="btn">Read more</span></article>
        <article><h3 class="item-title">News Flash # 2</h3><p>Maecenas faucibus mollis interdum. Morbi leo risus, porta ac consectetur ac, vestibulum at eros.</p><span class="btn">Read more</span></article>
        <article><h3 class="item-title">News Flash # 3</h3><p>Maecenas faucibus mollis interdum. Morbi leo risus, porta ac consectetur ac, vestibulum at eros.</p><span class="btn">Read more</span></article>
      </div>
    </section>
  </main>

  <main class="page page--right">
    <header class="spot-head" role="img" aria-label="Dark close-up of a keyboard">
      <svg width="15" height="15" viewBox="0 0 15 15"><circle cx="7.5" cy="7.5" r="7" fill="none" stroke="#fff" stroke-width=".8"/><rect x="5" y="4.5" width="5" height="6" fill="none" stroke="#fff" stroke-width=".7"/><line x1="5" y1="7.5" x2="10" y2="7.5" stroke="#fff" stroke-width=".7"/></svg>
      <span>SPOTLIGHT ON THE COUNTIES</span>
    </header>

    <section class="spot pad">
      <div class="spot__row">
        <div class="spot__text">
          <h3 class="item-title">Spotlight on the Counties # 1</h3>
          <p>Lorem ipsum dolor sit amet, consectetur adipiscing elit, sed do eiusmod tempor incididunt ut labore et dolore magna aliqua. Ut enim ad minim veniam. Duis aute irure dolor in reprehenderit.</p>
          <span class="btn">Read more</span>
        </div>
        <div class="photo" role="img" aria-label="Hands planting a seedling in soil" style="background:linear-gradient(135deg,#f3e2b8,#c88a3e 50%,#5a3c1e)"></div>
      </div>
      <div class="spot__row">
        <div class="photo" role="img" aria-label="Bridge at sunset" style="background:linear-gradient(135deg,#e7b3a6,#8e5b6e 50%,#3b2d3a)"></div>
        <div class="spot__text">
          <h3 class="item-title">Spotlight on the Counties # 2</h3>
          <p>Lorem ipsum dolor sit amet, consectetur adipiscing elit, sed do eiusmod tempor incididunt ut labore et dolore magna aliqua. Ut enim ad minim veniam. Duis aute irure dolor in reprehenderit.</p>
          <span class="btn">Read more</span>
        </div>
      </div>
    </section>

    <div class="band" style="height:30px">MWANACHI PERSPECTIVE</div>

    <section class="mwan pad">
      <article class="entry">
        <h3 class="item-title">Mwanachi Perspective</h3>
        <p>Lorem ipsum dolor sit amet, consectetur adipiscing elit, sed do eiusmod tempor incididunt ut labore et dolore magna aliqua. Ut enim ad minim veniam, quis nostrud exercitation ullamco laboris nisi ut aliquip ex ea commodo consequat. Duis aute irure dolor in reprehenderit in voluptate velit esse cillum dolore eu fugiat nulla pariatur. Excepteur sint occaecat cupidatat non proident, sunt in culpa qui officia deserunt mollit anim id est laborum. Sed ut perspiciatis unde omnis iste natus...</p>
        <span class="btn">Read more</span>
      </article>
      <article class="entry">
        <h3 class="item-title">Mwanachi Perspective</h3>
        <p>Lorem ipsum dolor sit amet, consectetur adipiscing elit, sed do eiusmod tempor incididunt ut labore et dolore magna aliqua. Ut enim ad minim veniam, quis nostrud exercitation ullamco laboris nisi ut aliquip ex ea commodo consequat. Duis aute irure dolor in reprehenderit in voluptate velit esse cillum dolore eu fugiat nulla pariatur. Excepteur sint occaecat cupidatat non proident, sunt in culpa qui officia deserunt mollit anim id est laborum. Sed ut perspiciatis unde omnis iste natus...</p>
        <span class="btn">Read more</span>
      </article>
    </section>

    <div class="band" style="height:32px">IMPORTANT DATES AND EVENTS</div>

    <section class="dates pad">
      <article><h3 class="item-title">Important Dates and Events<br># 1</h3><p>Maecenas faucibus mollis interdum. Morbi leo risus, porta ac consectetur ac, vestibulum at eros. Aenean eu leo quam. Pellentesque ornare sem lacinia quam venenatis vestibulum.</p><span class="btn">Read more</span></article>
      <article><h3 class="item-title">Important Dates and Events<br># 2</h3><p>Maecenas faucibus mollis interdum. Morbi leo risus, porta ac consectetur ac, vestibulum at eros. Aenean eu leo quam. Pellentesque ornare sem lacinia quam venenatis vestibulum.</p><span class="btn">Read more</span></article>
    </section>

    <section class="ceo pad">
      <div class="photo" role="img" aria-label="Portrait of the chief executive in an archive room"></div>
      <h3 class="item-title" style="margin-bottom:1px">CEO's Corner</h3>
      <div class="meta">Written by <b>CEO of Vaultnest</b> / February 2 2014</div>
      <p>Lorem ipsum dolor sit amet, consectetur adipiscing elit, sed do eiusmod tempor incididunt ut labore et dolore magna aliqua. Ut enim ad minim veniam, quis nostrud exercitation ullamco laboris nisi ut aliquip ex ea commodo consequat. Duis aute irure dolor in reprehenderit in voluptate velit esse cillum dolore eu fugiat nulla pariatur. Excepteur sint occaecat cupidatat non proident, sunt in culpa qui officia deserunt mollit anim id est laborum.</p>
      <span class="link">Read more</span>
      <div class="rule"></div>
    </section>

    <section class="signup pad">
      <div class="section-head">
        <h2 class="heading">Sign up for our<br>newsletter</h2>
        <div class="signup__form"><span>Enter your Email</span><b>SIGN UP!</b></div>
      </div>
      <p>Lorem ipsum dolor sit amet, consectetur adipiscing elit, sed do eiusmod tempor incididunt ut labore et dolore magna aliqua. Ut enim ad minim veniam.</p>
      <span class="link">Unsubscribe</span>
    </section>

    <footer class="footer">
      <h5>Contact</h5>
      <p>+254 700 123 456<br><a>hello@vaultnest.example</a></p>
      <div class="socials" aria-label="Social links"><i></i><i></i><i></i><i></i><i></i></div>
    </footer>
  </main>
</div>
</body>
</html>
```